Most Spectacularly Intriguing Website Ever

Alright, I'm a professional adventurer and a serial entrepreneur.
I am becoming a life coach and need an amazing website for my personal brand as an adventurer and entrepreneur as well as my life coaching.

I have previously kayaked a few major expeditions and launched a few businesses before. I want part of the website to be who I am and also what I can offer.

It needs to be amazing. Captivating. Intriguing. And most importantly make people say "I HAVE TO HIRE THIS GUY"!

You have full creative power. Use the deepest parts of your imagination. No particular colour schemes or themes in mind. So do whatever you like!

Industry/Entity Type

Life Coaching

Number of Pages Required

1 page

Requirements
Must have
• MUST be captivating, amazing, incredible.
Should not have
• Designs that are clearly just templates and stock standard mass produced designs will not be excepted. I am looking for something unique, with flare. That looks professionally made. Not like it is a template off a build your own website provider.

```html
<!DOCTYPE html>
<html lang="en">
<head>
<meta charset="utf-8">
<title>Dominic Ashford – Professional Adventurer</title>
<link href="https://fonts.googleapis.com/css2?family=Poppins:wght@400;500;600;700&family=Open+Sans:ital,wght@0,400;0,600;1,400&display=swap" rel="stylesheet">
<style>
:root{
  --blue:#1c4fa3;
  --blue-dark:#163f86;
  --orange:#f06b12;
  --ink:#222;
  --muted:#555;
  --light:#ebebeb;
  --footer:#121212;
  --white:#fff;
}
*{margin:0;padding:0;box-sizing:border-box}
html,body{width:1200px;height:3442px;overflow:hidden}
body{position:relative;font-family:'Open Sans',sans-serif;color:var(--ink);background:var(--white)}
.abs{position:absolute}
h1,h2,h3,h4{font-family:'Poppins',sans-serif}

/* hero */
.hero{left:0;top:0;width:1200px;height:633px;background:linear-gradient(180deg,#3d4d55 0%,#56614a 35%,#6b6a3e 60%,#4a4a2c 100%)}
.hero-shade{inset:0;background:rgba(0,0,0,.28)}
.logo{left:96px;top:28px;font-family:'Poppins',sans-serif;font-weight:600;font-size:32px;color:var(--white)}
.nav{right:96px;top:40px;display:flex;gap:38px;list-style:none}
.nav li{font-family:'Poppins',sans-serif;font-size:15px;font-weight:500;color:var(--white)}
.hero-title{left:0;width:1200px;top:296px;text-align:center;font-size:46px;font-weight:700;color:var(--white);letter-spacing:1px}
.hero-text{left:300px;width:600px;top:356px;text-align:center;font-size:14.5px;line-height:24px;color:var(--white)}
.btn-blue{background:var(--blue);color:var(--white);font-family:'Poppins',sans-serif;font-weight:600;font-size:16px;display:flex;align-items:center;justify-content:center}
.hero-btn{left:532px;top:420px;width:138px;height:37px}
.arrow{top:303px;width:36px;height:60px}

/* services */
.tile{width:600px;height:415px;text-align:center;color:var(--white)}
.tile-shade{inset:0;background:rgba(0,0,0,.35)}
.tile-kicker{left:0;width:600px;top:108px;font-family:'Poppins',sans-serif;font-size:22px}
.tile-title{left:0;width:600px;top:145px;font-size:25px;font-weight:700;letter-spacing:1px}
.tile-text{left:100px;width:400px;top:193px;font-size:13.5px;line-height:22px}
.tile-btn{left:231px;top:259px;width:138px;height:36px;border:2px solid var(--white);font-family:'Poppins',sans-serif;font-size:15px;font-weight:500;display:flex;align-items:center;justify-content:center}

/* about */
.about{left:0;top:1464px;width:1200px;height:477px;background:var(--light)}
.about-photo{left:179px;top:73px;width:330px;height:330px;border-radius:50%;border:6px solid var(--blue);background:linear-gradient(160deg,#8a6b4a,#5b4330 60%,#3b2c20)}
.about-title{left:553px;top:104px;font-size:31px;font-weight:600;letter-spacing:1px}
.about-lead{left:553px;top:155px;width:500px;font-size:14px;color:var(--muted);line-height:24px}
.about-body{left:553px;top:240px;width:500px;font-size:12.5px;color:var(--muted);line-height:23px}
.about-btn{left:553px;top:341px;width:106px;height:33px;font-size:12px;font-weight:500}

/* price */
.price-title{left:0;width:1200px;top:1993px;text-align:center;font-size:34px;font-weight:600;letter-spacing:1px}
.price-sub{left:0;width:1200px;top:2042px;text-align:center;font-size:12px;color:var(--muted)}
.card{top:2106px;width:303px;height:381px;border:3px solid var(--blue-dark);background:linear-gradient(160deg,#4a4f5c,#2d3340 55%,#3f3a34)}
.card-inner{left:19px;top:19px;width:259px;height:319px;background:rgba(255,255,255,.96)}
.amount{left:0;width:259px;top:20px;text-align:center;color:var(--blue);font-family:'Poppins',sans-serif}
.amount .cur{font-size:18px;vertical-align:14px}
.amount .big{font-size:40px}
.amount .per{font-size:15px}
.features{left:0;width:259px;top:88px;list-style:none}
.features li{height:36.5px;font-size:12.5px;color:var(--muted);display:flex;align-items:center;justify-content:center;gap:9px}
.card-btn{left:73px;top:293px;width:147px;height:35px;background:var(--orange);color:var(--white);font-family:'Poppins',sans-serif;font-weight:600;font-size:14px;display:flex;align-items:center;justify-content:center}

/* testimonial */
.testimonial{left:0;top:2574px;width:1200px;height:459px;background:linear-gradient(180deg,#1f55ab,#1a4998)}
.testi-title{left:0;width:1200px;top:45px;text-align:center;color:var(--white);font-size:32px;font-weight:600;letter-spacing:1px}
.testi-rule{left:565px;top:100px;width:70px;height:3px;background:var(--white)}
.avatar{top:156px;width:100px;height:100px;border-radius:50%;border:4px solid var(--white);background:linear-gradient(160deg,#b89478,#6e5444)}
.testi-name{top:170px;color:var(--white);font-family:'Poppins',sans-serif;font-size:17px}
.testi-role{top:200px;color:var(--white);font-size:13.5px}
.quote{left:300px;width:600px;top:290px;text-align:center;color:var(--white);font-style:italic;font-size:13px;line-height:26px}
.dot{top:403px;height:4px;background:rgba(255,255,255,.45)}

/* footer */
.footer{left:0;top:3033px;width:1200px;height:409px;background:var(--footer);color:var(--white)}
.foot-h{top:60px;font-size:20px;font-weight:600;letter-spacing:.5px}
.links{left:96px;top:114px;list-style:none}
.links li{height:22px;font-size:12.5px;display:flex;align-items:center;gap:12px}
.contact{left:328px;top:110px}
.contact-row{display:flex;gap:14px;font-size:13px;line-height:21px;margin-bottom:13px}
.socials{left:328px;top:257px;display:flex;gap:6px}
.socials span{width:22px;height:22px;border:1.5px solid #aaa;border-radius:50%}
.field{width:229px;height:41px;border:1.5px solid #888;font-size:12px;padding:0 14px;display:flex;align-items:center}
.submit{left:631px;top:227px;width:226px;height:41px;font-size:13px}
.copyright{left:0;width:1200px;top:360px;text-align:center;font-size:12px;color:#ccc}
</style>
</head>
<body>

<header class="abs hero" role="img" aria-label="Adventurer sitting among kangaroos on a grassy plain with forested hills">
  <div class="abs hero-shade"></div>
</header>
<div class="abs logo">Dominic Ashford</div>
<ul class="abs nav">
  <li>HOME</li><li>ABOUT ME</li><li>SERVICE</li><li>NEWS</li><li>COACHING</li><li>CONTACT</li>
</ul>
<svg class="abs arrow" style="left:70px" viewBox="0 0 36 60"><polyline points="30,4 6,30 30,56" fill="none" stroke="#fff" stroke-width="2"/></svg>
<svg class="abs arrow" style="left:1094px" viewBox="0 0 36 60"><polyline points="6,4 30,30 6,56" fill="none" stroke="#fff" stroke-width="2"/></svg>
<h1 class="abs hero-title">PROFESSIONAL ADVENTURER</h1>
<p class="abs hero-text">Nemo enim ipsam voluptatem quia voluptas sit aspernatur aut odit aut fugit, sed quia consequuntur magni dolores eos qui ratione voluptatem sequi nesciunt.</p>
<div class="abs btn-blue hero-btn">HIRE ME!</div>

<section class="abs tile" style="left:0;top:633px">
  <div class="abs" role="img" aria-label="Forest path lined with tall trees" style="inset:0;background:linear-gradient(160deg,#4b5a35,#6b6a3d 50%,#3a4128)"></div>
  <div class="abs tile-shade"></div>
  <div class="abs tile-kicker">Service</div>
  <h3 class="abs tile-title">LIFE COACHING</h3>
  <p class="abs tile-text">Nemo enim ipsam voluptatem quia voluptas sit aspeur aut odit aut fugit, sed quia consequuntur</p>
  <div class="abs tile-btn">READ MORE</div>
</section>
<section class="abs tile" style="left:600px;top:633px">
  <div class="abs" role="img" aria-label="Hikers on a red rocky ridge below snowy mountains" style="inset:0;background:linear-gradient(160deg,#6b7c95,#8a4a3a 45%,#5a2d24)"></div>
  <div class="abs tile-shade"></div>
  <div class="abs tile-kicker">Service</div>
  <h3 class="abs tile-title">EXPEDITIONS</h3>
  <p class="abs tile-text">Nemo enim ipsam voluptatem quia voluptas sit aspeur aut odit aut fugit, sed quia consequuntur</p>
  <div class="abs tile-btn">READ MORE</div>
</section>
<section class="abs tile" style="left:0;top:1048px">
  <div class="abs" role="img" aria-label="Hiker with backpack above a turquoise mountain lake" style="inset:0;background:linear-gradient(160deg,#4b6a86,#2f6f80 50%,#3a3a34)"></div>
  <div class="abs tile-shade"></div>
  <div class="abs tile-kicker">Service</div>
  <h3 class="abs tile-title">ADVENTURES</h3>
  <p class="abs tile-text">Nemo enim ipsam voluptatem quia voluptas sit aspeur aut odit aut fugit, sed quia consequuntur</p>
  <div class="abs tile-btn">READ MORE</div>
</section>
<section class="abs tile" style="left:600px;top:1048px">
  <div class="abs" role="img" aria-label="Team members working together in a workshop" style="inset:0;background:linear-gradient(160deg,#5a5550,#3d3733 50%,#6a5f55)"></div>
  <div class="abs tile-shade"></div>
  <div class="abs tile-kicker">Service</div>
  <h3 class="abs tile-title">ENTREPRENEUR</h3>
  <p class="abs tile-text">Nemo enim ipsam voluptatem quia voluptas sit aspeur aut odit aut fugit, sed quia consequuntur</p>
  <div class="abs tile-btn">READ MORE</div>
</section>

<section class="abs about">
  <div class="abs about-photo" role="img" aria-label="Portrait of the adventurer in a hat leaning on a wooden cabin"></div>
  <h2 class="abs about-title">ABOUT ME</h2>
  <p class="abs about-lead">I'm a professional adventurer and a serial entrepreneur.<br><span style="display:block;margin-top:8px;line-height:22px">I am becoming a life coach and need an amazing website for my personal brand as an adventurer and entrepreneur as well as my life coaching.</span></p>
  <p class="abs about-body">Sed ut perspiciatis unde omnis iste natus error sit voluptatem accusantium doloremque laudantium, totam rem aperiam, eaque ipsa quae ab illo inventore veritatis et quasi architecto beatae vitae dicta sunt explicabo.</p>
  <div class="abs btn-blue about-btn">READ MORE</div>
</section>

<h2 class="abs price-title">OUR PRICE</h2>
<p class="abs price-sub">Nemo enim ipsam voluptatem quia voluptas</p>

<svg width="0" height="0" style="position:absolute"><defs><symbol id="tick" viewBox="0 0 14 12"><polyline points="1,6 5,10 13,1" fill="none" stroke="#f06b12" stroke-width="3"/></symbol></defs></svg>

<div class="abs card" style="left:115px" role="img" aria-label="Outdoor landscape backdrop">
  <div class="abs card-inner">
    <div class="abs amount"><span class="cur">$</span><span class="big">100</span><span class="per">.00 Per Month</span></div>
    <ul class="abs features">
      <li><svg width="14" height="12"><use href="#tick"/></svg>Duis aute irure dolor</li>
      <li><svg width="14" height="12"><use href="#tick"/></svg>Nemo enim ipsam voluptatem</li>
      <li><svg width="14" height="12"><use href="#tick"/></svg>Sed ut perspiciatis unde</li>
      <li><svg width="14" height="12"><use href="#tick"/></svg>Duis aute irure dolor</li>
      <li><svg width="14" height="12"><use href="#tick"/></svg>Nemo enim ipsam voluptatem</li>
    </ul>
    <div class="abs card-btn">VIEW MORE</div>
  </div>
</div>
<div class="abs card" style="left:448px" role="img" aria-label="Outdoor landscape backdrop">
  <div class="abs card-inner">
    <div class="abs amount"><span class="cur">$</span><span class="big">99</span><span class="per">.00 Per Month</span></div>
    <ul class="abs features">
      <li><svg width="14" height="12"><use href="#tick"/></svg>Duis aute irure dolor</li>
      <li><svg width="14" height="12"><use href="#tick"/></svg>Nemo enim ipsam voluptatem</li>
      <li><svg width="14" height="12"><use href="#tick"/></svg>Sed ut perspiciatis unde</li>
      <li><svg width="14" height="12"><use href="#tick"/></svg>Duis aute irure dolor</li>
      <li><svg width="14" height="12"><use href="#tick"/></svg>Nemo enim ipsam voluptatem</li>
    </ul>
    <div class="abs card-btn">VIEW MORE</div>
  </div>
</div>
<div class="abs card" style="left:782px" role="img" aria-label="Outdoor landscape backdrop">
  <div class="abs card-inner">
    <div class="abs amount"><span class="cur">$</span><span class="big">150</span><span class="per">.00 Per Month</span></div>
    <ul class="abs features">
      <li><svg width="14" height="12"><use href="#tick"/></svg>Duis aute irure dolor</li>
      <li><svg width="14" height="12"><use href="#tick"/></svg>Nemo enim ipsam voluptatem</li>
      <li><svg width="14" height="12"><use href="#tick"/></svg>Sed ut perspiciatis unde</li>
      <li><svg width="14" height="12"><use href="#tick"/></svg>Duis aute irure dolor</li>
      <li><svg width="14" height="12"><use href="#tick"/></svg>Nemo enim ipsam voluptatem</li>
    </ul>
    <div class="abs card-btn">VIEW MORE</div>
  </div>
</div>

<section class="abs testimonial">
  <h2 class="abs testi-title">CLIENT TESTIMONIAL</h2>
  <div class="abs testi-rule"></div>
  <div class="abs avatar" style="left:186px" role="img" aria-label="Client portrait"></div>
  <div class="abs testi-name" style="left:307px">By John Doe</div>
  <div class="abs testi-role" style="left:307px">Nemo enim ipsam</div>
  <div class="abs avatar" style="left:485px" role="img" aria-label="Client portrait"></div>
  <svg class="abs" style="left:525px;top:258px" width="20" height="10"><polygon points="0,0 20,0 10,10" fill="#fff"/></svg>
  <div class="abs testi-name" style="left:606px">By John Doe</div>
  <div class="abs testi-role" style="left:606px">Nemo enim ipsam</div>
  <div class="abs avatar" style="left:783px" role="img" aria-label="Client portrait"></div>
  <div class="abs testi-name" style="left:906px">By John Doe</div>
  <div class="abs testi-role" style="left:906px">Nemo enim ipsam</div>
  <p class="abs quote">“ Lorem ipsum dolor sit amet, consectetur adipiscing elit, sed do eiusmod tempor incididunt ut labore et dolore magna aliqua. Ut enim ad minim veniam, quis nostrud exercitation ullamco laboris nisi ut aliquip ex ea commodo consequat. ”</p>
  <div class="abs dot" style="left:552px;width:30px;background:#fff"></div>
  <div class="abs dot" style="left:586px;width:30px"></div>
  <div class="abs dot" style="left:620px;width:30px"></div>
</section>

<footer class="abs footer">
  <h4 class="abs foot-h" style="left:96px">QUICK LINK</h4>
  <ul class="abs links">
    <li><svg width="6" height="9"><polyline points="1,1 5,4.5 1,8" fill="none" stroke="#fff" stroke-width="1.3"/></svg>Home</li>
    <li><svg width="6" height="9"><polyline points="1,1 5,4.5 1,8" fill="none" stroke="#fff" stroke-width="1.3"/></svg>About Us</li>
    <li><svg width="6" height="9"><polyline points="1,1 5,4.5 1,8" fill="none" stroke="#fff" stroke-width="1.3"/></svg>Services</li>
    <li><svg width="6" height="9"><polyline points="1,1 5,4.5 1,8" fill="none" stroke="#fff" stroke-width="1.3"/></svg>Price</li>
    <li><svg width="6" height="9"><polyline points="1,1 5,4.5 1,8" fill="none" stroke="#fff" stroke-width="1.3"/></svg>Blog</li>
    <li><svg width="6" height="9"><polyline points="1,1 5,4.5 1,8" fill="none" stroke="#fff" stroke-width="1.3"/></svg>Contact Us</li>
  </ul>
  <h4 class="abs foot-h" style="left:328px">CONTACT US</h4>
  <div class="abs contact">
    <div class="contact-row"><svg width="14" height="18" viewBox="0 0 14 18"><path d="M7 1a6 6 0 0 1 6 6c0 4-6 10-6 10S1 11 1 7a6 6 0 0 1 6-6z" fill="none" stroke="#fff" stroke-width="1.6"/><circle cx="7" cy="7" r="2" fill="#fff"/></svg><span>4417 Harbor Ridge Lane<br>12 Tampa, FL 33602</span></div>
    <div class="contact-row"><svg width="14" height="16" viewBox="0 0 14 16"><path d="M3 1l3 3-2 2c1 2 3 4 5 5l2-2 3 3-2 3C7 15 0 8 1 3z" fill="#fff"/></svg><span>Phone: 555-014-2271</span></div>
    <div class="contact-row"><svg width="14" height="14" viewBox="0 0 14 14"><rect x="1" y="3" width="12" height="9" fill="#fff"/><polyline points="1,3 7,8 13,3" fill="none" stroke="#121212" stroke-width="1.3"/></svg><span>hello@dominicashford.com</span></div>
  </div>
  <div class="abs socials"><span></span><span></span><span></span><span></span></div>
  <h4 class="abs foot-h" style="left:631px">GET FAST AND FREE PRICE QUOTE NOW!</h4>
  <div class="abs field" style="left:631px;top:117px">Your Name</div>
  <div class="abs field" style="left:872px;top:117px">Your E - Mail</div>
  <div class="abs field" style="left:631px;top:169px">Your Phone</div>
  <div class="abs field" style="left:872px;top:169px">Message</div>
  <div class="abs btn-blue submit">SUBMIT</div>
  <p class="abs copyright">©2017 Dominic Ashford, All Rights Reserved.</p>
</footer>

</body>
</html>
```